Business Card Design Project

I require a business card with the following information on them for various different people;
name
m:
f:
e:
I have a logo already and will attached that. We are in the construction industry. I require something clean and simple but eye catching at the same time. You can use another colour with our logo if you like and you can style the logo as well if you wish. I am open.
Also it needs to be front and back design.
Industry/Entity Type
Construction
Requirements
Must have
- Logo, name, mobile, fax and email address.
Front and back design

```html
<!DOCTYPE html>
<html lang="en">
<head>
<meta charset="utf-8">
<title>Stonebridge Developments – Business Cards</title>
<link rel="stylesheet" href="https://fonts.googleapis.com/css2?family=Questrial&display=swap">
<style>
  :root {
    --stage: #e6e7e8;
    --card-front: #ffffff;
    --card-back: #333333;
    --brand-green: #6cb33f;
    --text-light: #e8e8e8;
  }
  html, body {
    margin: 0;
    padding: 0;
    width: 1200px;
    height: 899px;
    overflow: hidden;
    background: var(--stage);
    font-family: "Questrial", "Helvetica Neue", Arial, sans-serif;
  }
  .stage {
    position: relative;
    width: 1200px;
    height: 899px;
  }
  .card {
    position: absolute;
    left: 335px;
    width: 532px;
    height: 302px;
    box-sizing: border-box;
  }
  .card--front {
    top: 96px;
    background: var(--card-front);
  }
  .card--back {
    top: 494px;
    background: var(--card-back);
  }
  .brand {
    position: absolute;
    display: flex;
    align-items: center;
    gap: 14px;
    color: var(--brand-green);
    white-space: nowrap;
  }
  .brand__square {
    display: block;
    background: var(--brand-green);
  }
  .card--front .brand {
    left: 18px;
    bottom: 20px;
    font-size: 34px;
  }
  .card--front .brand__square {
    width: 64px;
    height: 64px;
  }
  .card--back .brand {
    right: 20px;
    bottom: 18px;
    font-size: 25px;
  }
  .person {
    position: absolute;
    left: 34px;
    top: 50px;
    margin: 0;
  }
  .person__name {
    margin: 0;
    font-size: 23px;
    font-weight: 400;
    color: var(--brand-green);
    letter-spacing: 0.3px;
  }
  .person__role {
    margin: 4px 0 0;
    font-size: 17px;
    color: var(--text-light);
    letter-spacing: 0.4px;
  }
  .contact {
    position: absolute;
    left: 34px;
    top: 128px;
    margin: 0;
    padding: 0;
    list-style: none;
    font-size: 16.5px;
    line-height: 29px;
    color: var(--text-light);
    letter-spacing: 0.4px;
  }
  .contact__label {
    display: inline-block;
    width: 20px;
  }
</style>
</head>
<body>
<main class="stage">
  <section class="card card--front" aria-label="Card front">
    <div class="brand">
      <span class="brand__square" aria-hidden="true"></span>
      <span class="brand__name">Stonebridge Developments</span>
    </div>
  </section>

  <section class="card card--back" aria-label="Card back">
    <div class="person">
      <h1 class="person__name">Mark Ellison</h1>
      <p class="person__role">Managing Director</p>
    </div>
    <ul class="contact">
      <li><span class="contact__label">m</span>0412 555 019</li>
      <li><span class="contact__label">f</span>(02) 5550 1287</li>
      <li><span class="contact__label">e</span>mark@stonebridgedev.com.au</li>
    </ul>
    <div class="brand">
      <span class="brand__name">Stonebridge Developments</span>
    </div>
  </section>
</main>
</body>
</html>
```